Business card and stationery for School
Business card and stationery for School - Education
Creative Brief
Use same font as used in my logo
However variations is permitted
Bright & Fun-filled
Mrs Belinda T. Marrowfield
Proprietress
Plot 418C QX4 Temberlo Layout Opposite Pinwick Office Halverton Road, Dosumi FCT, Abuja
info@bluepebbleacademy.example
www.bluepebbleacademy.example

```html
<!DOCTYPE html>
<html lang="en">
<head>
<meta charset="utf-8">
<title>Blue Pebble Academy – Business Card</title>
<link href="https://fonts.googleapis.com/css2?family=Cinzel:wght@400;600;700&display=swap" rel="stylesheet">
<style>
  :root {
    --page-bg: #ecebe8;
    --card-white: #ffffff;
    --brand-purple: #8a2a8c;
    --deep-purple: #6e1f72;
    --brand-green: #6aa42f;
    --light-green: #9cc84a;
    --text-light: #ffffff;
    --pin-orange: #f1a51c;
  }
  * { box-sizing: border-box; margin: 0; padding: 0; }
  html, body { width: 1200px; height: 900px; overflow: hidden; }
  body {
    background: var(--page-bg);
    font-family: "Cinzel", serif;
    position: relative;
  }
  .business-card {
    position: absolute;
    left: 100px; top: 165px;
    width: 1000px; height: 570px;
    background: var(--card-white);
    box-shadow: 0 6px 24px rgba(0,0,0,0.12);
    overflow: hidden;
  }
  .card-waves { position: absolute; inset: 0; width: 1000px; height: 570px; }
  .brand-block {
    position: absolute;
    right: 60px; top: 70px;
    text-align: center;
  }
  .brand-row { display: flex; align-items: center; gap: 16px; justify-content: center; }
  .brand-dot {
    width: 44px; height: 44px; border-radius: 50%;
    background: var(--pin-orange);
  }
  .brand-name {
    font-weight: 600;
    font-size: 40px;
    color: var(--brand-purple);
    letter-spacing: 1px;
  }
  .brand-tagline {
    margin-top: 4px;
    font-size: 17px;
    color: var(--brand-green);
    letter-spacing: 0.5px;
  }
  .contact-list {
    position: absolute;
    left: 40px; top: 362px;
    list-style: none;
    color: var(--text-light);
    font-size: 13px;
    line-height: 19px;
    letter-spacing: 0.6px;
    text-transform: uppercase;
  }
  .contact-list li { display: flex; align-items: flex-start; gap: 10px; }
  .contact-icon {
    flex: 0 0 16px; width: 16px; height: 16px; margin-top: 1px;
  }
  .address-lines { display: block; }
  .holder {
    position: absolute;
    right: 60px; top: 396px;
    text-align: right;
    color: var(--text-light);
  }
  .holder-name { font-size: 19px; letter-spacing: 0.8px; }
  .holder-role { font-size: 14px; letter-spacing: 1px; margin-top: 4px; text-transform: uppercase; }
</style>
</head>
<body>
  <section class="business-card">
    <svg class="card-waves" viewBox="0 0 1000 570" aria-hidden="true">
      <path d="M0 300 C 220 250, 430 350, 650 310 C 800 282, 900 250, 1000 238 L1000 570 L0 570 Z" fill="var(--light-green)"/>
      <path d="M0 316 C 220 266, 430 366, 650 326 C 800 298, 900 268, 1000 258 L1000 570 L0 570 Z" fill="var(--card-white)"/>
      <path d="M0 326 C 230 286, 440 372, 660 336 C 810 310, 910 284, 1000 276 L1000 570 L0 570 Z" fill="var(--brand-green)"/>
      <path d="M0 342 C 240 300, 450 388, 670 350 C 820 325, 915 300, 1000 294 L1000 570 L0 570 Z" fill="var(--brand-purple)"/>
    </svg>

    <header class="brand-block">
      <div class="brand-row">
        <span class="brand-dot"></span>
        <span class="brand-name">BLUE PEBBLE ACADEMY</span>
      </div>
      <p class="brand-tagline">Learners Today, Leaders Tomorrow</p>
    </header>

    <ul class="contact-list">
      <li>
        <svg class="contact-icon" viewBox="0 0 16 16"><circle cx="8" cy="8" r="8" fill="#fff"/><path d="M8 3.5a3 3 0 0 0-3 3c0 2.2 3 5.5 3 5.5s3-3.3 3-5.5a3 3 0 0 0-3-3z" fill="var(--brand-purple)"/><circle cx="8" cy="6.5" r="1.1" fill="#fff"/></svg>
        <span class="address-lines">Plot 418C QX4 Temberlo Layout<br>Opposite Pinwick Office<br>Halverton Road, Dosumi<br>FCT, Abuja</span>
      </li>
      <li>
        <svg class="contact-icon" viewBox="0 0 16 16"><circle cx="8" cy="8" r="8" fill="#fff"/><path d="M5.2 4.2l1.4-.2.8 2-1 .8a5.5 5.5 0 0 0 2.8 2.8l.8-1 2 .8-.2 1.4c-3.8.4-7-2.8-6.6-6.6z" fill="var(--brand-purple)"/></svg>
        <span>+234 (09) 555 0142</span>
      </li>
      <li>
        <svg class="contact-icon" viewBox="0 0 16 16"><circle cx="8" cy="8" r="8" fill="#fff"/><rect x="5.5" y="3.5" width="5" height="9" rx="1" fill="var(--brand-purple)"/><rect x="6.4" y="4.6" width="3.2" height="5.6" fill="#fff"/></svg>
        <span>+234 800 555 0199</span>
      </li>
      <li>
        <svg class="contact-icon" viewBox="0 0 16 16"><circle cx="8" cy="8" r="8" fill="#fff"/><rect x="4" y="5" width="8" height="6" fill="var(--brand-purple)"/><path d="M4 5l4 3.3L12 5" stroke="#fff" stroke-width="0.9" fill="none"/></svg>
        <span>info@bluepebbleacademy.example</span>
      </li>
      <li>
        <svg class="contact-icon" viewBox="0 0 16 16"><circle cx="8" cy="8" r="8" fill="#fff"/><circle cx="8" cy="8" r="4" fill="none" stroke="var(--brand-purple)" stroke-width="1"/><path d="M4 8h8M8 4c-2 2.2-2 5.8 0 8M8 4c2 2.2 2 5.8 0 8" stroke="var(--brand-purple)" stroke-width="0.8" fill="none"/></svg>
        <span>www.bluepebbleacademy.example</span>
      </li>
    </ul>

    <div class="holder">
      <p class="holder-name">Mrs Belinda T. Marrowfield</p>
      <p class="holder-role">Proprietress</p>
    </div>
  </section>
</body>
</html>
```